Interior designer needs a power point template design

I need a template PowerPoint design for my client presentations. The presentations I prepare for my clients usually include the furniture project, the detail of the selected furniture, and the costs. There are a lot of images I insert. What I need is to have a template that I can use for all my presentations, where from time to time I will insert the specific images and descriptions I want to insert. What will always be the same will be the cover, the colors, the font, and the design of the internal sections.
I already have my logo that I would like to insert on each page of the presentation (in small size).
In summary, I need:
- basic template design
- cover with an image chosen by Pixelbarn photo
- design an internal section/chapter
- internal page design.

I like the clolors of pink and brown <8please see image attached)
Images (will come from Pixelbarn photo)
● entrance/hall
● living room
● dining room
● Bathroom
● Closet
● Kids room
● Master bedroom
● Master bathroom
● Kitchen
● Office
● Laundry
● Balcony or Terrace

Target Market(s)

Customers (both residential and commercial projects)

Industry/Entity Type

interior design

Font styles to use
Other font styles liked:
• I like courier new

Requirements
Must have
• beautiful design
Should not have
• animations

```html
<!DOCTYPE html>
<html lang="en">
<head>
<meta charset="utf-8">
<title>Stanza Chiara — Presentation Template</title>
<link href="https://fonts.googleapis.com/css2?family=Oswald:wght@200;300&family=Montserrat:wght@400;500&display=swap" rel="stylesheet">
<style>
  :root{
    --terracotta:#d8764f;
    --blush:#ea9284;
    --bar:#dc7d5a;
    --wine:#7f2118;
    --ink-light:rgba(255,255,255,.92);
    --line-light:rgba(255,255,255,.55);
    --footer-bg:#f2f2f2;
    --footer-ink:#555;
    --page-bg:#dcdadb;
    --display:'Oswald', 'Arial Narrow', sans-serif;
    --body:'Montserrat', Arial, sans-serif;
  }
  *{box-sizing:border-box;margin:0;padding:0}
  html,body{width:668px;height:1200px;overflow:hidden;background:var(--page-bg)}
  .canvas{position:relative;width:668px;height:1200px}

  .slide{position:absolute;width:301px;height:169px;overflow:hidden;background:#fff}
  .slide.col-left{left:28px}
  .slide.col-right{left:339px}
  .row-1{top:463px}.row-2{top:642px}.row-3{top:821px}.row-4{top:1000px}

  .hero{position:absolute;left:88px;top:46px;width:301px;height:169px;transform:scale(1.632);transform-origin:0 0}

  .fill{position:absolute}
  .grad-h{background:linear-gradient(90deg,var(--terracotta),var(--blush))}
  .grad-v{background:linear-gradient(180deg,var(--terracotta),var(--blush))}

  /* brand name: one line, one colour, one weight, with a plain circle */
  .brand{position:absolute;transform:translateX(-50%);display:flex;align-items:center;white-space:nowrap;color:var(--ink-light);font-family:var(--display);font-weight:300;line-height:1;letter-spacing:.08em}
  .brand-dot{border:.6px solid var(--ink-light);border-radius:50%;flex:none}
  .brand.lg{font-size:9px;gap:4px}
  .brand.lg .brand-dot{width:7px;height:7px}
  .brand.sm{font-size:5.6px;gap:2.5px}
  .brand.sm .brand-dot{width:4.5px;height:4.5px}

  /* type */
  .kicker{position:absolute;font-family:var(--display);font-weight:200;color:#fff;font-size:11px;letter-spacing:.01em}
  .title{position:absolute;font-family:var(--display);font-weight:200;color:#fff;font-size:19px;line-height:1;letter-spacing:.01em}
  .section-title{position:absolute;font-family:var(--display);font-weight:200;color:#fff;font-size:15px;line-height:1;transform:translateX(-50%);white-space:nowrap}
  .section-title.left{transform:none}
  .subtitle{position:absolute;font-family:var(--display);font-weight:200;color:#fff;font-size:6.4px;letter-spacing:.03em}
  .lead{position:absolute;font-family:var(--body);color:#fff;font-size:4.2px;line-height:1.15;text-align:center;transform:translateX(-50%);width:92px}
  .lead.wide{transform:none;text-align:left;width:215px}
  .date-pill{position:absolute;left:127px;top:105px;width:68px;height:10px;background:var(--wine);border-radius:1.5px;color:#f3c9bf;font-family:var(--display);font-weight:300;font-size:4.6px;letter-spacing:.05em;display:flex;align-items:center;justify-content:center}
  .rule{position:absolute;height:.5px;background:var(--line-light);opacity:.6}

  .slide-footer{position:absolute;left:0;bottom:0;width:100%;height:10px;background:var(--footer-bg);color:var(--footer-ink);font-family:var(--body);font-size:3.9px;letter-spacing:.03em;display:flex;align-items:center;justify-content:center}
  .page-bar{position:absolute;top:156px;height:5px;background:var(--bar);color:#fff;font-family:var(--body);font-size:2.5px;display:flex;align-items:center;justify-content:space-between;padding:0 3px}
  .page-num{opacity:.8;padding-right:8px}

  .photo{position:absolute;border:1px solid #fff;box-shadow:0 0 0 .3px rgba(0,0,0,.1)}
  .ph-bedroom{background:linear-gradient(160deg,#6b5a4e 0%,#d9d2c8 40%,#c9b8a2 75%,#8e8880 100%)}
  .ph-bath{background:linear-gradient(170deg,#f1f0ee 0%,#e6e3de 55%,#c9a98a 100%)}
  .ph-dining-a{background:linear-gradient(180deg,#e8ebe8 0%,#9aa59a 50%,#3b3a38 100%)}
  .ph-dining-b{background:linear-gradient(180deg,#8a8e8f 0%,#6e7274 50%,#b99877 100%)}
  .ph-kitchen-a{background:linear-gradient(180deg,#f1efec 0%,#e0ddd8 55%,#c7a88a 100%)}
  .ph-kitchen-b{background:linear-gradient(180deg,#ece9e4 0%,#d8cfc3 50%,#b89272 100%)}
  .ph-balcony-a{background:linear-gradient(135deg,#3a3532 0%,#d9d6d0 45%,#a9894f 100%)}
  .ph-balcony-b{background:linear-gradient(180deg,#f4f3f1 0%,#d6d4d0 55%,#d7a72e 100%)}
  .ph-kids-a{background:linear-gradient(180deg,#6fa39e 0%,#8db7b1 60%,#d6c6ad 100%)}
  .ph-kids-b{background:linear-gradient(180deg,#f2f0ec 0%,#e6e1d9 60%,#c9b59c 100%)}
  .ph-kids-c{background:linear-gradient(180deg,#eeeeea 0%,#d9d2c6 55%,#e889a6 100%)}

  .contact{position:absolute;left:126px;font-family:var(--body);color:#fff;font-size:4.4px;display:flex;align-items:center;gap:3px}
  .contact svg{width:5px;height:5px}
  .address{position:absolute;left:126px;top:89px;font-family:var(--display);font-weight:200;color:#fff;font-size:6px;letter-spacing:.01em}
</style>
</head>
<body>
<main class="canvas">

  <!-- Featured cover -->
  <section class="slide hero" aria-label="Cover slide">
    <div class="fill grad-h" style="left:0;top:0;width:301px;height:159px"></div>
    <div class="brand lg" style="left:60px;top:70px"><span class="brand-dot"></span><span>STANZA CHIARA</span></div>
    <p class="kicker" style="left:127px;top:40px">STANZA CHIARA</p>
    <h1 class="title" style="left:127px;top:58px">PRESENTATION TITLE</h1>
    <div class="rule" style="left:120px;top:81px;width:160px"></div>
    <p class="subtitle" style="left:127px;top:88px">SUBTITLE OF PRESENTATION GOES HERE!</p>
    <div class="date-pill">FRIDAY, APRIL 15, 2022</div>
    <footer class="slide-footer">© 2022 STANZA CHIARA, All rights reserved.</footer>
  </section>

  <!-- Cover -->
  <section class="slide col-left row-1" aria-label="Cover slide">
    <div class="fill grad-h" style="left:0;top:0;width:301px;height:159px"></div>
    <div class="brand lg" style="left:60px;top:70px"><span class="brand-dot"></span><span>STANZA CHIARA</span></div>
    <p class="kicker" style="left:127px;top:40px">STANZA CHIARA</p>
    <h2 class="title" style="left:127px;top:58px">PRESENTATION TITLE</h2>
    <div class="rule" style="left:120px;top:81px;width:160px"></div>
    <p class="subtitle" style="left:127px;top:88px">SUBTITLE OF PRESENTATION GOES HERE!</p>
    <div class="date-pill">FRIDAY, APRIL 15, 2022</div>
    <footer class="slide-footer">© 2022 STANZA CHIARA, All rights reserved.</footer>
  </section>

  <!-- Bedroom -->
  <section class="slide col-right row-1" aria-label="Bedroom section">
    <div class="fill grad-v" style="left:0;top:0;width:150px;height:169px"></div>
    <div class="brand sm" style="left:62px;top:58px"><span class="brand-dot"></span><span>STANZA CHIARA</span></div>
    <h2 class="section-title" style="left:62px;top:93px">BEDROOM</h2>
    <p class="lead" style="left:62px;top:113px">Lorem ipsum dolor sit amet, consectetur adipiscing elit. Vivamus eu dui ex.</p>
    <div class="photo ph-bedroom" role="img" aria-label="Photo of a bright bedroom with beamed ceiling" style="left:125px;top:7px;width:169px;height:140px"></div>
    <div class="page-bar" style="left:7px;width:294px"><span>© 2022 STANZA CHIARA, All rights reserved.</span><span class="page-num">| 2</span></div>
  </section>

  <!-- Bathroom -->
  <section class="slide col-left row-2" aria-label="Bathroom section">
    <div class="fill grad-v" style="left:150px;top:0;width:151px;height:169px"></div>
    <div class="brand sm" style="left:238px;top:58px"><span class="brand-dot"></span><span>STANZA CHIARA</span></div>
    <h2 class="section-title" style="left:238px;top:93px">BATHROOM</h2>
    <p class="lead" style="left:238px;top:113px">Lorem ipsum dolor sit amet, consectetur adipiscing elit. Vivamus eu dui ex.</p>
    <div class="photo ph-bath" role="img" aria-label="Photo of a white bathroom with freestanding tub" style="left:7px;top:7px;width:169px;height:140px"></div>
    <div class="page-bar" style="left:7px;width:294px"><span>© 2022 STANZA CHIARA, All rights reserved.</span><span class="page-num">| 3</span></div>
  </section>

  <!-- Dining room -->
  <section class="slide col-right row-2" aria-label="Dining room section">
    <div class="fill grad-h" style="left:0;top:0;width:301px;height:84px"></div>
    <div class="brand sm" style="left:33px;top:33px"><span class="brand-dot"></span><span>STANZA CHIARA</span></div>
    <h2 class="section-title left" style="left:68px;top:27px">DINING ROOM</h2>
    <p class="lead wide" style="left:68px;top:47px">Lorem ipsum dolor sit amet, consectetur adipiscing elit. Vivamus eu dui ex. Curabitur dapibus dignissim dui, in molestie metus feugiat sed. Praesent aliquet lorem ex, eu dapibus odio varius.</p>
    <div class="photo ph-dining-a" role="img" aria-label="Photo of a dining room with large windows" style="left:7px;top:91px;width:141px;height:56px"></div>
    <div class="photo ph-dining-b" role="img" aria-label="Photo of a dining table with grey chairs" style="left:153px;top:91px;width:141px;height:56px"></div>
    <div class="page-bar" style="left:7px;width:294px"><span>© 2022 STANZA CHIARA, All rights reserved.</span><span class="page-num">| 4</span></div>
  </section>

  <!-- Kitchen -->
  <section class="slide col-left row-3" aria-label="Kitchen section">
    <div class="fill grad-v" style="left:0;top:0;width:150px;height:169px"></div>
    <div class="brand sm" style="left:62px;top:58px"><span class="brand-dot"></span><span>STANZA CHIARA</span></div>
    <h2 class="section-title" style="left:62px;top:93px">KITCHEN</h2>
    <p class="lead" style="left:62px;top:113px">Lorem ipsum dolor sit amet, consectetur adipiscing elit. Vivamus eu dui ex.</p>
    <div class="photo ph-kitchen-a" role="img" aria-label="Photo of a kitchen with island and pendant lamps" style="left:125px;top:7px;width:169px;height:67px"></div>
    <div class="photo ph-kitchen-b" role="img" aria-label="Photo of a kitchen with wooden table" style="left:125px;top:80px;width:169px;height:67px"></div>
    <div class="page-bar" style="left:7px;width:294px"><span>© 2022 STANZA CHIARA, All rights reserved.</span><span class="page-num">| 5</span></div>
  </section>

  <!-- Balcony -->
  <section class="slide col-right row-3" aria-label="Balcony section">
    <div class="fill grad-v" style="left:150px;top:0;width:151px;height:169px"></div>
    <div class="brand sm" style="left:238px;top:58px"><span class="brand-dot"></span><span>STANZA CHIARA</span></div>
    <h2 class="section-title" style="left:238px;top:93px">BALCONY</h2>
    <p class="lead" style="left:238px;top:113px">Lorem ipsum dolor sit amet, consectetur adipiscing elit. Vivamus eu dui ex.</p>
    <div class="photo ph-balcony-a" role="img" aria-label="Photo of a terrace lounge with plants" style="left:7px;top:7px;width:169px;height:67px"></div>
    <div class="photo ph-balcony-b" role="img" aria-label="Photo of a balcony with yellow sofa" style="left:7px;top:80px;width:169px;height:67px"></div>
    <div class="page-bar" style="left:7px;width:294px"><span>© 2022 STANZA CHIARA, All rights reserved.</span><span class="page-num">| 6</span></div>
  </section>

  <!-- Kids room -->
  <section class="slide col-left row-4" aria-label="Kids room section">
    <div class="fill grad-h" style="left:0;top:0;width:301px;height:103px"></div>
    <div class="brand sm" style="left:33px;top:33px"><span class="brand-dot"></span><span>STANZA CHIARA</span></div>
    <h2 class="section-title left" style="left:68px;top:27px">KIDS ROOM</h2>
    <p class="lead wide" style="left:68px;top:47px">Lorem ipsum dolor sit amet, consectetur adipiscing elit. Vivamus eu dui ex. Curabitur dapibus dignissim dui, in molestie metus feugiat sed. Praesent aliquet lorem ex, eu dapibus odio varius.</p>
    <div class="photo ph-kids-a" role="img" aria-label="Photo of a kids room with teal wall" style="left:11px;top:72px;width:91px;height:62px"></div>
    <div class="photo ph-kids-b" role="img" aria-label="Photo of a bright kids room with toys" style="left:105px;top:72px;width:91px;height:62px"></div>
    <div class="photo ph-kids-c" role="img" aria-label="Photo of a playroom with pink rug" style="left:199px;top:72px;width:91px;height:62px"></div>
    <div class="page-bar" style="left:7px;width:294px"><span>© 2022 STANZA CHIARA, All rights reserved.</span><span class="page-num">| 7</span></div>
  </section>

  <!-- Contact -->
  <section class="slide col-right row-4" aria-label="Contact slide">
    <div class="fill grad-h" style="left:0;top:0;width:301px;height:159px"></div>
    <div class="brand lg" style="left:60px;top:78px"><span class="brand-dot"></span><span>STANZA CHIARA</span></div>
    <p class="kicker" style="left:126px;top:41px">STANZA</p>
    <h2 class="title" style="left:126px;top:58px">CHIARA</h2>
    <div class="rule" style="left:120px;top:82px;width:160px"></div>
    <p class="address">DI MARTA CELANI, VIA DEI TIGLI, 24</p>
    <p class="contact" style="top:100px"><svg viewBox="0 0 10 10" aria-hidden="true"><path d="M2 1l2 2-1 1.5c.6 1.3 1.3 2 2.5 2.5L7 6l2 2-1.2 1.2C4.5 9 1 5.5.8 2.2z" fill="#fff"/></svg>340/5518820</p>
    <p class="contact" style="top:109px"><svg viewBox="0 0 10 10" aria-hidden="true"><circle cx="5" cy="5" r="4" fill="none" stroke="#fff" stroke-width="1"/><circle cx="5" cy="5" r="1.6" fill="none" stroke="#fff" stroke-width="1"/></svg>martacelani@studiomail.com</p>
    <p class="contact" style="top:118px"><svg viewBox="0 0 10 10" aria-hidden="true"><circle cx="5" cy="5" r="4" fill="none" stroke="#fff" stroke-width=".8"/><ellipse cx="5" cy="5" rx="1.8" ry="4" fill="none" stroke="#fff" stroke-width=".8"/><path d="M1 5h8" stroke="#fff" stroke-width=".8"/></svg>www.martacelani.com</p>
    <footer class="slide-footer">© 2022 STANZA CHIARA, All rights reserved.</footer>
  </section>

</main>
</body>
</html>
```